8 x 8 - Social Media Posting - Bright Key DPA Program

Buyer(s) Need Down Payment Assistance?
OUR BRIGHTKEY PROGRAM
offers all you need....
* Grant Up to 3.5% of Purchase Price
* No Down Payment (FHA Only)
* 600 Minimum Score
* No Max DTI Requirement (As Determined by AUS)
* No First Time Home Buyer Requirement
* No Minimum Borrower Contribution
* Non Occupant Co-Borrowers Allowed
Call us today at (800) 417-2960
Harborlane Lending Services, Inc.
7200 Wexmoor Road, Larkfield, VA 22190
www.harborlanelend.example
NMLS #318674

```html
<!DOCTYPE html>
<html lang="en">
<head>
<meta charset="utf-8">
<title>Bright Key DPA Program</title>
<link href="https://fonts.googleapis.com/css2?family=Montserrat:wght@500;600;700;800&display=swap" rel="stylesheet">
<style>
  :root {
    --ink: #03141d;
    --lime: #a4cf38;
    --sky: #1b9ae0;
    --white: #ffffff;
  }
  * { margin: 0; padding: 0; box-sizing: border-box; }
  html, body { width: 1200px; height: 1200px; overflow: hidden; background: var(--ink); }
  body { font-family: "Montserrat", sans-serif; color: var(--white); }
  .post { position: relative; width: 1200px; height: 1200px; overflow: hidden; }
  .hero-photo {
    position: absolute; inset: 0 0 300px 0;
    background:
      linear-gradient(180deg, rgba(255,255,255,0) 55%, #5f8a3a 100%),
      linear-gradient(90deg, #dcdfe3 0%, #eef0f2 30%, #6f7f95 45%, #5d6d84 70%, #6b7b90 100%);
  }
  .roof { position: absolute; inset: 0; width: 1200px; height: 1200px; }
  .brand {
    position: absolute; left: 120px; top: 655px; width: 310px;
    display: flex; align-items: center; justify-content: center; gap: 10px;
    font-weight: 700; font-size: 20px; color: var(--white); white-space: nowrap;
  }
  .brand-dot { width: 14px; height: 14px; border-radius: 50%; background: var(--lime); flex: none; }
  .question { position: absolute; left: 97px; top: 739px; }
  .question span {
    display: block; width: max-content; background: var(--sky);
    font-weight: 800; font-size: 39px; line-height: 46px; height: 46px;
    padding: 0 13px; margin-bottom: 10px; letter-spacing: 0.5px;
  }
  .program {
    position: absolute; left: 97px; top: 908px;
    font-weight: 800; font-size: 50px; line-height: 57px; color: var(--lime);
    letter-spacing: 0.2px; white-space: nowrap;
  }
  .call-label { position: absolute; left: 97px; top: 1040px; font-weight: 700; font-size: 20px; color: var(--sky); }
  .phone {
    position: absolute; left: 97px; top: 1075px; display: flex; align-items: center; gap: 6px;
    font-weight: 700; font-size: 41px;
  }
  .website {
    position: absolute; left: 97px; top: 1130px; display: flex; align-items: center; gap: 10px;
    font-weight: 500; font-size: 24px;
  }
  .website b { color: var(--lime); font-weight: 500; }
  .offers { position: absolute; left: 598px; top: 722px; font-weight: 700; font-size: 42px; }
  .features { position: absolute; left: 598px; top: 785px; list-style: none; }
  .features li {
    display: flex; align-items: center; gap: 12px;
    font-weight: 500; font-size: 19.5px; height: 35.3px;
  }
  .features svg { width: 20px; height: 18px; flex: none; }
  .divider { position: absolute; left: 602px; top: 1057px; width: 511px; height: 1px; background: var(--white); }
  .office { position: absolute; left: 596px; top: 1070px; display: flex; gap: 20px; }
  .office-name { font-weight: 700; font-size: 18.5px; color: var(--sky); }
  .office-address { font-weight: 500; font-size: 18px; margin-top: 4px; }
  .nmls {
    display: inline-block; margin-top: 10px; background: var(--sky);
    font-weight: 700; font-size: 19px; line-height: 35px; padding: 0 10px;
  }
</style>
</head>
<body>
<main class="post">
  <div class="hero-photo" role="img" aria-label="Smiling family of five holding new house keys on the front lawn of a blue-grey suburban home with a white garage door"></div>

  <svg class="roof" viewBox="0 0 1200 1200" aria-hidden="true">
    <polygon points="0,656 297,352 1200,673 1200,1200 0,1200" fill="#ffffff"/>
    <polygon points="0,667 299,364 1200,687 1200,1200 0,1200" fill="#a4cf38"/>
    <polygon points="0,749 313,429 1200,749 1200,1200 0,1200" fill="#03141d"/>
  </svg>

  <div class="brand"><span class="brand-dot"></span>Harborlane Lending Services</div>

  <h1 class="question">
    <span>BUYER’S NEED</span>
    <span>DOWN PAYMENT</span>
    <span>ASSISTANCE?</span>
  </h1>

  <h2 class="program">OUR BRIGHTKEY<br>PROGRAM</h2>

  <p class="call-label">CALL US TODAY AT</p>
  <p class="phone">
    <svg width="32" height="32" viewBox="0 0 24 24" fill="none" stroke="#fff" stroke-width="2.2" stroke-linecap="round"><path d="M5 3l3 0 1.5 4-2 1.5a11 11 0 0 0 6 6l1.5-2 4 1.5v3a2 2 0 0 1-2 2A16 16 0 0 1 3 5a2 2 0 0 1 2-2z"/><path d="M15 3a6 6 0 0 1 6 6M15 7a2 2 0 0 1 2 2"/></svg>
    (800) 417-2960
  </p>
  <p class="website">
    <svg width="26" height="26" viewBox="0 0 24 24" fill="none"><circle cx="12" cy="12" r="11" stroke="#fff" stroke-width="1.5"/><circle cx="12" cy="12" r="7.5" fill="#a4cf38"/><path d="M4.5 12h15M12 4.5v15M7 8h10M7 16h10" stroke="#03141d" stroke-width="1"/></svg>
    <span>www.<b>harborlanelend</b>.example</span>
  </p>

  <h2 class="offers">offers all you need....</h2>
  <ul class="features">
    <li><svg viewBox="0 0 20 18"><path d="M10 1L1 9h3v8h4v-5h4v5h4V9h3z" fill="#a4cf38"/></svg>Grant Up to 3.5% of Purchase Price</li>
    <li><svg viewBox="0 0 20 18"><path d="M10 1L1 9h3v8h4v-5h4v5h4V9h3z" fill="#a4cf38"/></svg>No Down Payment (FHA Only)</li>
    <li><svg viewBox="0 0 20 18"><path d="M10 1L1 9h3v8h4v-5h4v5h4V9h3z" fill="#a4cf38"/></svg>600 Minimum Score</li>
    <li><svg viewBox="0 0 20 18"><path d="M10 1L1 9h3v8h4v-5h4v5h4V9h3z" fill="#a4cf38"/></svg>No Max DTI Requirement (As Determined by AUS)</li>
    <li><svg viewBox="0 0 20 18"><path d="M10 1L1 9h3v8h4v-5h4v5h4V9h3z" fill="#a4cf38"/></svg>No First Time Home Buyer Requirement</li>
    <li><svg viewBox="0 0 20 18"><path d="M10 1L1 9h3v8h4v-5h4v5h4V9h3z" fill="#a4cf38"/></svg>No Minimum Borrower Contribution</li>
    <li><svg viewBox="0 0 20 18"><path d="M10 1L1 9h3v8h4v-5h4v5h4V9h3z" fill="#a4cf38"/></svg>Non Occupant Co-Borrowers Allowed</li>
  </ul>

  <div class="divider"></div>
  <div class="office">
    <svg width="30" height="30" viewBox="0 0 30 30" fill="none"><circle cx="15" cy="15" r="14" stroke="#fff" stroke-width="1.5"/><path d="M15 7a5 5 0 0 0-5 5c0 4 5 10 5 10s5-6 5-10a5 5 0 0 0-5-5z" fill="#a4cf38"/><circle cx="15" cy="12" r="1.8" fill="#03141d"/></svg>
    <div>
      <p class="office-name">Harborlane Lending Services, Inc.</p>
      <p class="office-address">7200 Wexmoor Road, Larkfield, VA 22190</p>
      <p class="nmls">NMLS #318674</p>
    </div>
  </div>
</main>
</body>
</html>
```